Coral Ridge Networks Ltd

I need a website that is an informational only. We are a construction business building telecommunications sites. Seeing how our company is Coral Ridge the color blue might want to be incorporated in the color scheme.
I can provide more picture of towers and wireless communications if needed.
current website www.coralridgenet.ca

Industry/Entity Type

Wireless Telecommunications, Construction

Coding

Coded - Design and coding required

Number of Pages Required

2 page

Font styles to use
Sans Serif

Colors

Designer to choose colors to be used in the design.

```html
<!DOCTYPE html>
<html lang="en">
<head>
<meta charset="utf-8">
<title>Coral Ridge Networks Ltd</title>
<link rel="stylesheet" href="https://fonts.googleapis.com/css2?family=Jost:wght@300;400&family=Roboto:wght@400;500;700&display=swap">
<style>
:root{
  --navy:#2b3a8f;
  --blue:#3a63c4;
  --sky:#5a9be0;
  --ink:#1d1d1f;
  --grey:#6b6b73;
  --pale:#f3f4f8;
  --white:#ffffff;
  --btn:linear-gradient(90deg,#2b3a8f,#4f8fdc);
}
*{box-sizing:border-box;margin:0;padding:0}
html,body{width:1200px;height:3960px;overflow:hidden}
body{position:relative;font-family:"Roboto",Arial,sans-serif;color:var(--ink);background:var(--white)}
.abs{position:absolute}
.btn{position:absolute;display:flex;align-items:center;justify-content:center;gap:8px;background:var(--btn);color:var(--white);font:500 13px "Roboto",Arial,sans-serif;text-transform:uppercase;border-radius:24px;border:2px solid rgba(255,255,255,.7);box-shadow:0 3px 8px rgba(40,60,140,.25)}
.btn .dot{width:12px;height:12px;border-radius:50%;background:var(--white);position:relative}
.btn .dot::after{content:"";position:absolute;left:4px;top:3px;border-left:5px solid var(--navy);border-top:3px solid transparent;border-bottom:3px solid transparent}
.sect-title{position:absolute;left:0;width:1200px;text-align:center;font:300 38px "Jost",Arial,sans-serif;color:var(--ink)}
.rule{position:absolute;width:54px;height:12px}
.rule::before{content:"";position:absolute;left:0;right:0;top:5px;height:2px;background:var(--sky)}
.rule::after{content:"";position:absolute;left:22px;top:1px;width:10px;height:10px;border-radius:50%;background:var(--navy)}

/* header */
.site-header{position:absolute;left:0;top:0;width:1200px;height:94px;background:var(--white)}
.brand{position:absolute;left:111px;top:0;width:200px;height:128px;background:var(--white);display:flex;align-items:center;justify-content:center;gap:10px;z-index:3;box-shadow:0 2px 6px rgba(0,0,0,.06)}
.brand-mark{width:16px;height:16px;border-radius:50%;background:var(--blue)}
.brand-name{font:400 25px "Roboto",Arial,sans-serif;color:var(--blue)}
.nav{position:absolute;left:394px;top:37px;display:flex;gap:33px;font:500 14px "Roboto",Arial,sans-serif;color:var(--ink)}
.nav .active{color:var(--blue)}
.call{position:absolute;left:900px;top:23px;width:187px;height:48px;border-radius:24px;background:var(--navy);color:var(--white);font:700 14px "Roboto",Arial,sans-serif;display:flex;align-items:center;padding-left:12px;gap:18px}
.call .ico{width:30px;height:30px;border-radius:50%;background:var(--sky);display:flex;align-items:center;justify-content:center}

/* hero */
.hero{position:absolute;left:0;top:94px;width:1200px;height:644px;background:linear-gradient(180deg,#3b4a9c 0%,#6a6fc0 35%,#b8b6e6 70%,#eeeefa 100%)}
.hero h1{position:absolute;left:0;top:185px;width:1200px;text-align:center;font:300 53px/57px "Jost",Arial,sans-serif;color:var(--white)}
.hero p{position:absolute;left:0;top:320px;width:1200px;text-align:center;font:500 17px/26px "Roboto",Arial,sans-serif;color:var(--white)}

/* services */
.services{position:absolute;left:0;top:738px;width:1200px;height:1377px;background:linear-gradient(180deg,#ffffff 0%,#f2f3f8 50%,#eceef5 100%)}
.svc-photo{position:absolute;width:404px;height:404px;border-radius:50%;border:5px solid var(--white);box-shadow:0 0 0 1px #d6d9e6,0 8px 20px rgba(40,50,100,.15)}
.svc-badge{position:absolute;left:112px;top:112px;width:170px;height:170px;border-radius:50%;background:linear-gradient(160deg,#2b3a8f,#4f8fdc);display:flex;align-items:center;justify-content:center}
.svc-text{position:absolute;width:470px}
.svc-text h2{font:500 30px "Roboto",Arial,sans-serif;color:var(--ink)}
.svc-text .bar{width:40px;height:3px;background:var(--sky);margin:16px 0 26px}
.svc-text p{font:400 15px/25px "Roboto",Arial,sans-serif;color:var(--grey);text-align:justify}

/* about */
.about{position:absolute;left:0;top:2115px;width:1200px;height:557px;background:linear-gradient(90deg,#4c5d9e 0%,#3d4d8e 40%,#24306e 65%,#141c47 100%)}
.about h2{position:absolute;left:111px;top:80px;font:300 38px "Jost",Arial,sans-serif;color:var(--white)}
.about .wrule{position:absolute;left:111px;top:128px;width:54px;height:12px}
.about .wrule::before{content:"";position:absolute;left:0;right:0;top:5px;height:2px;background:var(--white)}
.about .wrule::after{content:"";position:absolute;left:20px;top:0;width:12px;height:12px;border-radius:50%;background:var(--white)}
.about .copy{position:absolute;left:111px;top:165px;width:485px;font:500 17px/24px "Roboto",Arial,sans-serif;color:var(--white);text-align:justify}
.about .copy p{margin-bottom:24px}

/* why */
.why{position:absolute;left:0;top:2672px;width:1200px;height:900px;background:linear-gradient(180deg,#fff 0%,#fff 75%,#eceef3 100%)}
.why .lead{position:absolute;left:111px;top:160px;width:978px;text-align:center;font:400 15px/24px "Roboto",Arial,sans-serif;color:var(--grey)}
.feat{position:absolute;width:240px;text-align:center}
.ring{width:190px;height:190px;margin:0 auto;border-radius:50%;background:linear-gradient(160deg,#2b3a8f,#5aa0e6);display:flex;align-items:center;justify-content:center}
.ring .inner{width:156px;height:156px;border-radius:50%;background:var(--white);display:flex;align-items:center;justify-content:center}
.feat h3{margin-top:28px;font:500 17px/24px "Roboto",Arial,sans-serif;color:var(--ink)}

/* footer */
.site-footer{position:absolute;left:0;top:3572px;width:1200px;height:388px;background:#2d3a8e;color:var(--white)}
.f-brand{position:absolute;left:180px;top:80px;display:flex;align-items:center;gap:8px}
.f-brand .m{width:14px;height:14px;border-radius:50%;background:var(--white)}
.f-brand span{font:400 26px "Roboto",Arial,sans-serif}
.socials{position:absolute;left:161px;top:3772px;display:flex;gap:14px}
.socials i{display:block;width:35px;height:35px;border:1px solid rgba(255,255,255,.7)}
.col{position:absolute;top:60px}
.col h4{font:500 19px "Roboto",Arial,sans-serif}
.col .bar{width:28px;height:3px;background:var(--white);margin:10px 0 18px}
.col li{list-style:none;font:400 13px/31px "Roboto",Arial,sans-serif;display:flex;gap:10px;align-items:flex-start}
.col li::before{content:"»";font-size:13px}
.col.contact li::before{content:none}
.col.contact li{line-height:20px;margin-bottom:16px}
.col.contact svg{flex:none;margin-top:3px}
.f-line{position:absolute;left:111px;top:318px;width:978px;height:1px;background:rgba(255,255,255,.5)}
.f-bottom{position:absolute;left:111px;top:335px;width:978px;display:flex;justify-content:space-between;font:400 14px "Roboto",Arial,sans-serif}
</style>
</head>
<body>

<header class="site-header">
  <div class="brand"><span class="brand-mark"></span><span class="brand-name">Coral Ridge</span></div>
  <nav class="nav"><span class="active">Home</span><span>About Us</span><span>Our Services</span><span>Why Choose Us</span><span>Contact</span></nav>
  <div class="call"><span class="ico"><svg width="14" height="14" viewBox="0 0 24 24"><path fill="#fff" d="M6.6 10.8a15 15 0 0 0 6.6 6.6l2.2-2.2c.3-.3.7-.4 1-.2 1.1.4 2.3.6 3.6.6.6 0 1 .4 1 1V20c0 .6-.4 1-1 1A17 17 0 0 1 3 4c0-.6.4-1 1-1h3.5c.6 0 1 .4 1 1 0 1.3.2 2.5.6 3.6.1.3 0 .7-.2 1z"/></svg></span>1-604-555-0142</div>
</header>

<section class="hero" role="img" aria-label="Telecommunication towers framing a city skyline in violet light">
  <h1>Coral Ridge is committed<br>to a strong safety policy</h1>
  <p>At Coral Ridge Ltd, we are dedicated to providing our customers<br>with friendly professional service.</p>
  <div class="btn" style="left:522px;top:391px;width:156px;height:43px">Contact Us <span class="dot"></span></div>
</section>

<section class="services">
  <h2 class="sect-title" style="top:40px">Our Services</h2>
  <div class="rule" style="left:573px;top:82px"></div>

  <div class="svc-photo" role="img" aria-label="Rooftop antenna installation overlooking mountains" style="left:160px;top:130px;background:linear-gradient(180deg,#4a86d6 0%,#9cc0e6 45%,#7d7f80 70%,#4a4b4d 100%)">
    <div class="svc-badge"><svg width="90" height="90" viewBox="0 0 90 90" fill="#fff"><rect x="28" y="10" width="34" height="16"/><rect x="12" y="30" width="66" height="50"/><g fill="#3a63c4"><rect x="20" y="40" width="8" height="10"/><rect x="34" y="40" width="8" height="10"/><rect x="48" y="40" width="8" height="10"/><rect x="62" y="40" width="8" height="10"/><rect x="20" y="58" width="8" height="10"/><rect x="48" y="58" width="8" height="10"/><rect x="62" y="58" width="8" height="10"/><rect x="36" y="58" width="10" height="22"/><rect x="36" y="14" width="18" height="8"/></g></svg></div>
  </div>
  <div class="svc-text" style="left:621px;top:225px">
    <h2>Rooftop Sites</h2><div class="bar"></div>
    <p>Structural upgrades or simple ballast mounts. Shelter on the ground, leasehold build outs or cabinets on the roof.&nbsp; Coral Ridge can install what you need where you need it</p>
  </div>
  <div class="btn" style="left:623px;top:389px;width:158px;height:43px">Find Out More <span class="dot"></span></div>

  <div class="svc-photo" role="img" aria-label="Lattice tower with antennas against blue sky" style="left:658px;top:516px;background:linear-gradient(180deg,#3f72c8 0%,#7fa9dd 50%,#c7ccd2 100%)">
    <div class="svc-badge"><svg width="90" height="90" viewBox="0 0 90 90" fill="none" stroke="#fff" stroke-width="5" stroke-linecap="round"><circle cx="45" cy="28" r="5" fill="#fff"/><path d="M33 18a16 16 0 0 0 0 20M57 18a16 16 0 0 1 0 20M25 12a26 26 0 0 0 0 32M65 12a26 26 0 0 1 0 32M45 34 30 80M45 34l15 46M36 62h18M33 72h24"/></svg></div>
  </div>
  <div class="svc-text" style="left:115px;top:612px">
    <h2>Towers and Monopoles</h2><div class="bar"></div>
    <p>Coral Ridge can engineer, supply and install all your tower needs. New structures or existing, call us for pricing we would be happy to help out</p>
  </div>
  <div class="btn" style="left:116px;top:775px;width:158px;height:43px">Find Out More <span class="dot"></span></div>

  <div class="svc-photo" role="img" aria-label="Antenna mast on a building with clouds and mountains behind" style="left:160px;top:903px;background:linear-gradient(180deg,#2f63c2 0%,#6b9be0 45%,#dfe6ef 65%,#7b8590 100%)">
    <div class="svc-badge"><svg width="90" height="90" viewBox="0 0 90 90" fill="#fff"><rect x="12" y="36" width="26" height="46"/><rect x="42" y="12" width="36" height="70"/><g fill="#3a63c4"><rect x="18" y="44" width="6" height="6"/><rect x="27" y="44" width="6" height="6"/><rect x="18" y="56" width="6" height="6"/><rect x="27" y="56" width="6" height="6"/><rect x="18" y="68" width="6" height="6"/><rect x="27" y="68" width="6" height="6"/><rect x="49" y="22" width="7" height="7"/><rect x="63" y="22" width="7" height="7"/><rect x="49" y="36" width="7" height="7"/><rect x="63" y="36" width="7" height="7"/><rect x="49" y="50" width="7" height="7"/><rect x="63" y="50" width="7" height="7"/><rect x="49" y="64" width="7" height="7"/><rect x="63" y="64" width="7" height="7"/></g></svg></div>
  </div>
  <div class="svc-text" style="left:621px;top:997px">
    <h2>In Building</h2><div class="bar"></div>
    <p>Small office or large Hotel.&nbsp; Coral Ridge has installed services into all size buildings.&nbsp; Fiber, cat6, or coax, we have the abilities to install, test, and get the job done</p>
  </div>
  <div class="btn" style="left:623px;top:1161px;width:158px;height:43px">Find Out More <span class="dot"></span></div>
</section>

<section class="about" role="img" aria-label="Worker looking over a night city skyline with network lines">
  <h2>About Us</h2>
  <div class="wrule"></div>
  <div class="copy">
    <p>At Coral Ridge Ltd, we are dedicated to providing our customers with friendly professional service. We value your business. We have made it our mission to provide reliable products and services in our customer-driven approach.</p>
    <p>Our courteous, professional team is able to support a range of services to meet your requirements.</p>
    <p>To learn more about Coral Ridge Ltd, and the products and services we can offer, please call us at 1-604-555-0142.</p>
  </div>
  <div class="btn" style="left:112px;top:427px;width:156px;height:44px">Learn More <span class="dot"></span></div>
</section>

<section class="why">
  <h2 class="sect-title" style="top:82px">Why Choose Us</h2>
  <div class="rule" style="left:573px;top:127px"></div>
  <p class="lead">At Coral Ridge Networks Ltd Safety is number one.&nbsp; Coral Ridge Ltd is committed to a strong safety policy, protecting its staff and the general public from accidents and harm.&nbsp; All Coral Ridge Employees are certified “Tower Competent Climber and Rescue”.&nbsp; In addition to tower safety and fall protection Coral Ridge's safety training and practices include but are not limited to the following</p>

  <div class="feat" style="left:115px;top:283px"><div class="ring"><div class="inner"><svg width="70" height="70" viewBox="0 0 70 70"><circle cx="35" cy="30" r="22" fill="#3a63c4"/><circle cx="35" cy="30" r="14" fill="#fff"/><path d="M28 30l5 5 9-10" stroke="#3a63c4" stroke-width="4" fill="none"/><path d="M22 48l-6 16 9-3 5 7 5-16zM48 48l6 16-9-3-5 7-5-16z" fill="#5a9be0"/></svg></div></div><h3>COR Certified</h3></div>
  <div class="feat" style="left:358px;top:283px"><div class="ring"><div class="inner"><svg width="70" height="70" viewBox="0 0 70 70"><rect x="8" y="20" width="54" height="40" rx="4" fill="#3a63c4"/><rect x="24" y="12" width="22" height="10" rx="3" fill="none" stroke="#3a63c4" stroke-width="4"/><circle cx="35" cy="40" r="12" fill="#fff"/><path d="M35 33v14M28 40h14" stroke="#3a63c4" stroke-width="4"/></svg></div></div><h3>BC Level 1 first aid</h3></div>
  <div class="feat" style="left:602px;top:283px"><div class="ring"><div class="inner"><svg width="80" height="70" viewBox="0 0 80 70"><path d="M14 18h38v32H14zM52 28h14l8 10v12H52z" fill="#3a63c4"/><circle cx="24" cy="52" r="7" fill="#5a9be0"/><circle cx="62" cy="52" r="7" fill="#5a9be0"/><path d="M2 26h10M4 34h8" stroke="#3a63c4" stroke-width="3"/></svg></div></div><h3>Transportation Endorsement<br>first aid</h3></div>
  <div class="feat" style="left:845px;top:283px"><div class="ring"><div class="inner"><svg width="70" height="70" viewBox="0 0 70 70" fill="#3a63c4"><rect x="12" y="38" width="8" height="18"/><rect x="24" y="30" width="8" height="26"/><rect x="36" y="22" width="8" height="34"/><rect x="48" y="12" width="8" height="44"/><rect x="8" y="60" width="52" height="3" fill="#5a9be0"/></svg></div></div><h3>Sprat Level 1</h3></div>

  <div class="feat" style="left:235px;top:560px"><div class="ring"><div class="inner"><svg width="80" height="70" viewBox="0 0 80 70" fill="#3a63c4"><circle cx="40" cy="14" r="6"/><circle cx="18" cy="24" r="6"/><circle cx="62" cy="24" r="6"/><rect x="20" y="34" width="40" height="14" fill="#5a9be0"/><circle cx="26" cy="56" r="5"/><circle cx="54" cy="56" r="5"/><rect x="10" y="32" width="8" height="20"/><rect x="62" y="32" width="8" height="20"/></svg></div></div><h3>On site tailboard meeting</h3></div>
  <div class="feat" style="left:479px;top:560px"><div class="ring"><div class="inner"><svg width="70" height="70" viewBox="0 0 70 70"><path d="M35 6l24 9v18c0 15-10 25-24 31C21 58 11 48 11 33V15z" fill="#3a63c4"/><circle cx="35" cy="34" r="12" fill="none" stroke="#fff" stroke-width="3"/><path d="M29 34l4 4 8-8" stroke="#fff" stroke-width="3" fill="none"/></svg></div></div><h3>Monthly in office safety<br>meetings</h3></div>
  <div class="feat" style="left:723px;top:560px"><div class="ring"><div class="inner"><svg width="70" height="70" viewBox="0 0 70 70"><rect x="8" y="22" width="54" height="36" rx="4" fill="#3a63c4"/><rect x="24" y="14" width="22" height="10" rx="3" fill="none" stroke="#3a63c4" stroke-width="4"/><rect x="8" y="36" width="54" height="4" fill="#5a9be0"/><rect x="30" y="33" width="10" height="10" fill="#fff"/></svg></div></div><h3>Job site specific hazard<br>assessment</h3></div>
</section>

<footer class="site-footer">
  <div class="f-brand"><span class="m"></span><span>Coral Ridge</span></div>
  <div class="col" style="left:435px"><h4>Quick Links</h4><div class="bar"></div>
    <ul><li>Home</li><li>About Us</li><li>Our Services</li><li>Why Us</li><li>Contact Us</li></ul></div>
  <div class="col" style="left:623px"><h4>Our Services</h4><div class="bar"></div>
    <ul><li>Rooftop Sites</li><li>Towers and Monopoles</li><li>In Building</li></ul></div>
  <div class="col contact" style="left:843px"><h4>Contact Us</h4><div class="bar"></div>
    <ul>
      <li><svg width="12" height="14" viewBox="0 0 24 28"><path fill="#fff" d="M12 0a10 10 0 0 0-10 10c0 8 10 18 10 18s10-10 10-18A10 10 0 0 0 12 0zm0 14a4 4 0 1 1 0-8 4 4 0 0 1 0 8z"/></svg><span>4410 Harbourview Rd Fernvale, BC<br>V2Y1K3</span></li>
      <li><svg width="13" height="13" viewBox="0 0 24 24"><path fill="#fff" d="M6.6 10.8a15 15 0 0 0 6.6 6.6l2.2-2.2c.3-.3.7-.4 1-.2 1.1.4 2.3.6 3.6.6.6 0 1 .4 1 1V20c0 .6-.4 1-1 1A17 17 0 0 1 3 4c0-.6.4-1 1-1h3.5c.6 0 1 .4 1 1 0 1.3.2 2.5.6 3.6.1.3 0 .7-.2 1z"/></svg><span>Tel No :&nbsp; 1-604-555-0142</span></li>
      <li><svg width="14" height="11" viewBox="0 0 24 18"><path fill="#fff" d="M0 0h24v18H0zM2 2l10 8 10-8"/><path d="M2 2l10 8 10-8" stroke="#2d3a8e" stroke-width="2" fill="none"/></svg><span>Email :&nbsp; info@coralridgenet.ca</span></li>
    </ul></div>
  <div class="f-line"></div>
  <div class="f-bottom"><span>© 2022 Coral Ridge. All Rights Reserved</span><span>Privacy Policy &nbsp;|&nbsp; Terms &amp; Conditions</span></div>
</footer>
<div class="socials"><i></i><i></i><i></i><i></i></div>

</body>
</html>
```